依頼詳細
会社の新名刺のデザインを募集させて頂きます。弊社はデザイナーズ物件の管理をメインに行っている業者ですので、スタイリッシュなデザインのご提案を希望します。また、沢山のイメージから選定させて頂きたいので、不動産業という枠にとらわれない、新しいデザインを頂けますと幸いです。またロゴの色がピンクとグレーで構成されておりますが、こちらの色見は名刺デザインにあまり反映させたくはないので、そちらご考慮頂いたデザインの提案を頂けますと幸いです。(弊社のロゴデータを添付させて頂きます)また今回の名刺は縦型で作成したく思います。何卒よろしくお願い申し上げます。
記載項目
会社名/事業部名/役職/名前/住所/会社電話番号/携帯電話番号/fax番号/mail/宅地建物取引番号/事業内容/ホームページURL
希望イメージ
シンプル 複雑
単色 カラフル
暗い 明るい
日常 高級
遊び心 厳粛
未来的 伝統的
女性的 男性的
希望する色
今のロゴのピンク味を主張せず、名刺を一新したカラー希望です。
納品ファイル
• 高解像度JPG (.jpg)
• PNG形式 (.png)
補足説明
こちらに弊社のロゴデータ添付させて頂きますんので、ご確認のうえご提案の程よろしくお願い致します。

シックなデザインに社内の投票にて多数賛同を得たため当選させて頂きました。

この度は皆さま、沢山の素敵なご提案誠にありがとうございました。またご依頼した際はご提案、ご応募お待ち申し上げます。何卒宜しくお願い致します。

```html
<!DOCTYPE html>
<html lang="ja">
<head>
<meta charset="utf-8">
<title>株式会社 ベルモント様 名刺デザイン</title>
<link href="https://fonts.googleapis.com/css2?family=Noto+Sans+JP:wght@400;700&family=Noto+Serif+JP:wght@400;600&display=swap" rel="stylesheet">
<style>
:root{
  --ink:#222;
  --muted:#555;
  --green:#2f9a4a;
  --green-light:#bfe3c6;
  --accent:#2b2b3a;
  --rule:#cfcfcf;
  --card-edge:#dcdcdc;
  --bg:#ffffff;
}
*{margin:0;padding:0;box-sizing:border-box}
html,body{width:867px;height:1200px;overflow:hidden;background:var(--bg)}
body{position:relative;font-family:"Noto Sans JP",sans-serif;color:var(--ink)}
.sheet-title{position:absolute;left:32px;top:84px;display:flex;align-items:center;gap:12px;font-size:20px;font-weight:700;letter-spacing:.04em}
.sheet-title::before{content:"";width:7px;height:26px;background:var(--accent)}
.card{position:absolute;top:419px;width:232px;height:420px;background:#fff;border:1px solid var(--card-edge);box-shadow:0 1px 4px rgba(0,0,0,.12);overflow:hidden}
.card--front{left:182px}
.card--back{left:451px}
.card-label{position:absolute;top:850px;font-size:14px;font-weight:700}
.card-label--front{left:182px}
.card-label--back{left:451px}
.front-band{position:absolute;right:0;top:0;width:100px;height:100%;background:linear-gradient(90deg,rgba(47,154,74,0) 0%,var(--green-light) 30%,var(--green) 100%)}
.front-wordmark{position:absolute;right:6px;top:50%;transform:translateY(-50%);writing-mode:vertical-rl;font-family:"Noto Sans JP",sans-serif;font-weight:700;font-size:58px;letter-spacing:.06em;color:#fff}
.front-info{position:absolute;left:16px;top:40px;font-family:"Noto Serif JP",serif}
.role{font-size:8px;color:var(--muted)}
.name{font-size:22px;font-weight:600;margin-top:16px;letter-spacing:.08em}
.name-roman{font-size:9px;letter-spacing:.12em;color:var(--muted);margin-top:2px}
.contact{font-size:7px;color:var(--muted);margin-top:18px;line-height:1.7}
.brand{position:absolute;left:16px;top:262px;display:flex;align-items:center;gap:6px}
.brand-mark{width:20px;height:20px;background:var(--green)}
.brand-name{font-size:13px;font-weight:700;line-height:1.1;color:var(--ink)}
.brand-name small{display:block;font-size:7px;font-weight:700}
.address{position:absolute;left:16px;top:300px;font-size:6.5px;line-height:1.7;color:var(--muted)}
.back-brand{position:absolute;left:0;right:0;top:28px;text-align:center}
.back-brand .brand-mark{margin:0 auto 6px}
.back-brand .brand-name{font-size:12px}
.back-lead{position:absolute;left:20px;right:20px;top:90px;font-size:6.5px;text-align:center;line-height:1.6;color:var(--muted)}
.back-section{position:absolute;left:20px;right:20px;font-size:6.5px;line-height:1.7;color:var(--muted)}
.back-section h3{font-size:7px;color:var(--ink);margin-bottom:4px}
.biz{top:140px}
.biz dl{display:grid;grid-template-columns:42px 1fr;row-gap:4px;padding-bottom:4px;border-bottom:1px solid var(--rule)}
.license{top:300px}
.url{top:345px}
.foot-rule{position:absolute;left:183px;top:1179px;width:500px;height:1px;background:var(--rule)}
</style>
</head>
<body>
<h1 class="sheet-title">株式会社 ベルモント様　名刺デザイン</h1>

<section class="card card--front">
  <div class="front-band"></div>
  <div class="front-wordmark">BELMONT</div>
  <div class="front-info">
    <p class="role">代表取締役社長</p>
    <p class="name">佐倉 直人</p>
    <p class="name-roman">NAOTO SAKURA</p>
    <p class="contact">MOBILE.090-0000-0000<br>E.mail.sakura@belmont.example</p>
  </div>
  <div class="brand">
    <span class="brand-mark"></span>
    <span class="brand-name">BELMONT<small>株式会社ベルモント</small></span>
  </div>
  <p class="address">東京都千代田区神田1-2-3<br>ベルモントビル 5F<br>TEL.03-0000-0000<br>FAX.03-0000-0001<br>URL.www.belmont.example<br>宅地建物取引業 東京都知事(1)第00000号</p>
</section>

<section class="card card--back">
  <div class="back-brand">
    <span class="brand-mark" style="display:block"></span>
    <span class="brand-name">BELMONT</span>
  </div>
  <p class="back-lead">デザイナーズ物件の管理を中心に、<br>住まいの新しい価値をご提案します。</p>
  <div class="back-section biz">
    <h3>事業内容</h3>
    <dl>
      <dt>賃貸管理</dt><dd>物件の募集・契約・入居者対応</dd>
      <dt>売買仲介</dt><dd>土地・建物の売買仲介</dd>
      <dt>企画設計</dt><dd>リノベーションの企画提案</dd>
    </dl>
    <p style="margin-top:8px">住まいの価値を高める総合的なサービスをお届けします。</p>
  </div>
  <div class="back-section license">
    <h3>免許</h3>
    <p>宅地建物取引業 東京都知事(1)第00000号</p>
  </div>
  <div class="back-section url">
    <h3>Web</h3>
    <p>www.belmont.example</p>
  </div>
</section>

<p class="card-label card-label--front">■名刺 / 表</p>
<p class="card-label card-label--back">■名刺 / 裏</p>
<div class="foot-rule"></div>
</body>
</html>
```